BHAG Poster

We like creativity and visual boxes and shapes not just bullet points. We think we want it to be landscape view. Here are some of the parameters:

BHAG:
Become one of the most admired construction companies in the markets we serve within the next 10 years

3 – 5 year goals:
1. Generate 35m in revenue by 2020
2. Have a 50/50 mix of Public-Private job mix
3. Maintain 15% annual growth

1 year goals:
1. $24M in revenue with better margins
2. 14% gross margin on year
3. Business development begins to pay off
4. Continue recruiting great & talented people

Dynamic Quarter Goal:
(Leave this area blank so we can fill it in each quarter please)

Industry/Entity Type

Landscape

Colors
0355a3

Requirements
Must have
• SHAPES OR BOXES FOR VISUAL EFFECT. We don't want it to just be words on a page. Must be creative. Must have our logo somewhere on the poster. Our cmyk blue color is 100-80-0-22. Poster can have different colors, but it just needs to have some of our blue in it.
Should not have
• no bullet points

```html
<!DOCTYPE html>
<html lang="en">
<head>
<meta charset="utf-8">
<title>Harwell Construction – BHAG Poster</title>
<link rel="stylesheet" href="https://fonts.googleapis.com/css2?family=Oswald:wght@400;500;600;700&family=Lato:wght@400;700&display=swap">
<style>
  :root {
    --brand-navy: #1a2e8a;
    --brand-deep: #0f1f6e;
    --brand-mid: #2a46a8;
    --rule-grey: #7a7a7a;
    --band-grey: #6b6b6b;
    --ink: #1e1e1e;
    --paper: #ffffff;
    --backdrop: #dcdcdc;
    --sky-top: #c9d8e6;
    --sky-low: #eef2f5;
    --facade: #d8d6d0;
  }
  html, body {
    margin: 0;
    width: 1200px;
    height: 1200px;
    overflow: hidden;
    background: var(--backdrop);
  }
  .canvas {
    position: relative;
    width: 1200px;
    height: 1200px;
  }
  .poster {
    position: absolute;
    left: 40px;
    top: 202px;
    width: 1295px;
    height: 920px;
    transform: scale(0.8649);
    transform-origin: top left;
    background: var(--paper);
    overflow: hidden;
    box-shadow: 0 6px 18px rgba(0,0,0,0.25);
  }
  .poster__shapes {
    position: absolute;
    inset: 0;
  }
  .brand {
    position: absolute;
    left: 530px;
    top: 352px;
    display: flex;
    align-items: center;
    gap: 8px;
  }
  .brand__square {
    width: 54px;
    height: 58px;
    background: var(--brand-navy);
  }
  .brand__name {
    font-family: "Oswald", sans-serif;
    font-weight: 600;
    color: var(--brand-navy);
    line-height: 1;
    text-align: center;
  }
  .brand__name-main {
    display: block;
    font-size: 44px;
    letter-spacing: 0.5px;
  }
  .brand__name-sub {
    display: block;
    font-size: 16px;
    letter-spacing: 0.5px;
    margin-top: 2px;
  }
  .bhag {
    position: absolute;
    left: 0;
    right: 0;
    top: 420px;
    text-align: center;
  }
  .bhag__title {
    margin: 0;
    font-family: "Oswald", sans-serif;
    font-weight: 700;
    font-size: 62px;
    line-height: 1.1;
    color: var(--brand-navy);
  }
  .bhag__statement {
    margin: 2px 0 0;
    font-family: "Oswald", sans-serif;
    font-weight: 500;
    font-size: 18px;
    line-height: 23px;
    color: var(--ink);
  }
  .goal-badge {
    position: absolute;
    width: 106px;
    height: 106px;
    border: 2px solid var(--brand-navy);
    border-radius: 50%;
    background: var(--paper);
    display: flex;
    flex-direction: column;
    align-items: center;
    justify-content: center;
    font-family: "Oswald", sans-serif;
    color: var(--brand-navy);
    line-height: 1.15;
  }
  .goal-badge__span { font-weight: 700; font-size: 25px; }
  .goal-badge__label { font-weight: 400; font-size: 20px; }
  .goal-badge--long { left: 109px; top: 550px; }
  .goal-badge--year { left: 726px; top: 550px; }
  .goal-list {
    position: absolute;
    margin: 0;
    padding: 0;
    list-style: none;
    font-family: "Lato", sans-serif;
    font-size: 18px;
    line-height: 27px;
    color: var(--ink);
  }
  .goal-list__item span { display: inline-block; width: 26px; }
  .goal-list--long { left: 239px; top: 560px; }
  .goal-list--year { left: 861px; top: 543px; }
  .section-label {
    position: absolute;
    margin: 0;
    font-family: "Oswald", sans-serif;
    font-weight: 600;
    font-size: 19px;
    color: var(--brand-navy);
    top: 700px;
  }
  .section-label--quarter { left: 241px; }
  .section-label--contact { left: 732px; }
  .quarter-box {
    position: absolute;
    left: 239px;
    top: 737px;
    width: 392px;
    height: 139px;
    border: 2px solid var(--brand-navy);
  }
  .contact {
    position: absolute;
    left: 732px;
    top: 732px;
    margin: 0;
    padding: 0;
    list-style: none;
    font-family: "Lato", sans-serif;
    color: var(--ink);
  }
  .contact__row {
    display: flex;
    align-items: center;
    height: 25.5px;
  }
  .contact__icon {
    width: 16px;
    height: 16px;
    margin: 0 14px 0 2px;
    flex: none;
  }
  .contact__row--phone { font-size: 21px; height: 24px; }
  .contact__row--mail, .contact__row--web, .contact__row--address { font-size: 15px; }
  .contact__row--social { font-size: 13.5px; }
  .social-dot {
    width: 11px;
    height: 11px;
    border-radius: 50%;
    background: var(--brand-navy);
    margin: 0 17px 0 4px;
    flex: none;
  }
</style>
</head>
<body>
<div class="canvas">
  <main class="poster">
    <svg class="poster__shapes" width="1295" height="920" viewBox="0 0 1295 920">
      <defs>
        <linearGradient id="photoTone" x1="0" y1="0" x2="0" y2="1">
          <stop offset="0" stop-color="var(--sky-top)"/>
          <stop offset="0.35" stop-color="var(--sky-low)"/>
          <stop offset="0.6" stop-color="var(--facade)"/>
          <stop offset="1" stop-color="#8e8f8c"/>
        </linearGradient>
      </defs>

      <rect class="hero-photo" x="0" y="0" width="1295" height="380" fill="url(#photoTone)" role="img" aria-label="Photograph of a single-storey white building with a pitched roof, tall black-framed windows and glass entry doors under a cloudy sky"/>

      <polygon class="panel panel--left" points="0,95 470,375 0,575" fill="var(--brand-navy)"/>
      <polygon class="panel panel--right" points="1295,95 825,375 1295,575" fill="var(--brand-navy)"/>
      <line x1="0" y1="95" x2="470" y2="375" stroke="var(--rule-grey)" stroke-width="6"/>
      <line x1="1295" y1="95" x2="825" y2="375" stroke="var(--rule-grey)" stroke-width="6"/>

      <polygon class="chevron-white" points="0,575 647,300 1295,575 1295,920 0,920" fill="var(--paper)"/>
      <polyline points="552,336 647,298 742,336" fill="none" stroke="var(--brand-navy)" stroke-width="3"/>

      <polygon class="corner corner--left" points="0,810 162,793 115,920 0,920" fill="var(--brand-navy)"/>
      <polygon class="corner corner--right" points="1147,793 1295,813 1295,920 1192,920" fill="var(--brand-navy)"/>
      <polygon points="127,903 1187,903 1192,920 122,920" fill="var(--band-grey)"/>
    </svg>

    <div class="brand">
      <div class="brand__square"></div>
      <div class="brand__name">
        <span class="brand__name-main">HARWELL</span>
        <span class="brand__name-sub">CONSTRUCTION</span>
      </div>
    </div>

    <section class="bhag">
      <h1 class="bhag__title">BHAG</h1>
      <p class="bhag__statement">Become one of the most admired construction companies in the<br>markets we serve within the next 10 years</p>
    </section>

    <div class="goal-badge goal-badge--long">
      <span class="goal-badge__span">3 – 5</span>
      <span class="goal-badge__label">YEAR</span>
      <span class="goal-badge__label">GOALS</span>
    </div>
    <ol class="goal-list goal-list--long">
      <li class="goal-list__item"><span>1.</span>Generate 35m in revenue by 2020</li>
      <li class="goal-list__item"><span>2.</span>Have a 50/50 mix of Public-Private job mix</li>
      <li class="goal-list__item"><span>3.</span>Maintain 15% annual growth</li>
    </ol>

    <div class="goal-badge goal-badge--year">
      <span class="goal-badge__span">1</span>
      <span class="goal-badge__label">YEAR</span>
      <span class="goal-badge__label">GOALS</span>
    </div>
    <ol class="goal-list goal-list--year">
      <li class="goal-list__item"><span>1.</span>$24M in revenue with better margins</li>
      <li class="goal-list__item"><span>2.</span>14% gross margin on year</li>
      <li class="goal-list__item"><span>3.</span>Business development begins to pay off</li>
      <li class="goal-list__item"><span>4.</span>Continue recruiting great &amp; talented people</li>
    </ol>

    <h2 class="section-label section-label--quarter">DYNAMIC QUARTER GOAL:</h2>
    <div class="quarter-box"></div>

    <h2 class="section-label section-label--contact">CONTACT:</h2>
    <ul class="contact">
      <li class="contact__row contact__row--phone">
        <svg class="contact__icon" viewBox="0 0 16 16"><path d="M3 2h3l1 3-2 1.5a9 9 0 0 0 4.5 4.5L11 9l3 1v3a1 1 0 0 1-1 1A12 12 0 0 1 2 3a1 1 0 0 1 1-1z" fill="var(--brand-navy)"/></svg>
        <span>+61 2 8555 0142</span>
      </li>
      <li class="contact__row contact__row--mail">
        <svg class="contact__icon" viewBox="0 0 16 16"><rect x="1.5" y="3.5" width="13" height="9" fill="none" stroke="var(--brand-navy)" stroke-width="1.6"/><path d="M1.5 3.5 8 9l6.5-5.5" fill="none" stroke="var(--brand-navy)" stroke-width="1.6"/></svg>
        <span>info@harwellconstruction.com</span>
      </li>
      <li class="contact__row contact__row--web">
        <svg class="contact__icon" viewBox="0 0 16 16" fill="none" stroke="var(--brand-navy)" stroke-width="1.3"><circle cx="8" cy="8" r="6.5"/><ellipse cx="8" cy="8" rx="3" ry="6.5"/><path d="M1.5 8h13M2.5 4.8h11M2.5 11.2h11"/></svg>
        <span>www.harwellconstruction.com</span>
      </li>
      <li class="contact__row contact__row--address">
        <svg class="contact__icon" viewBox="0 0 16 16"><path d="M8 1a5 5 0 0 0-5 5c0 4 5 9 5 9s5-5 5-9a5 5 0 0 0-5-5zm0 7a2 2 0 1 1 0-4 2 2 0 0 1 0 4z" fill="var(--brand-navy)"/></svg>
        <span>27 Ridgeline Avenue, Miranda Sydney NSW 2228</span>
      </li>
      <li class="contact__row contact__row--social">
        <span class="social-dot"></span>
        <span>/harwellbuild</span>
      </li>
      <li class="contact__row contact__row--social">
        <span class="social-dot"></span>
        <span>/harwellbuild</span>
      </li>
    </ul>
  </main>
</div>
</body>
</html>
```